DJ Promotional Flyer for Booking and promotional purposes

This promotional flyer would be used for Instagram or any other social media websites. I would like would like it to be used for booking purposes. My logo should be a big part of this flyer. As well as my contact information. Which would my email: djkvoss478@mailbright.net, Wavecrate: wavecrate.com/djkvoss, Instagram: DJMARLOKVOSS and the rest I will send by private message.

Target Market(s)

Club owners, or party promoters

Industry/Entity Type

Night Club

Font styles to use
Sans Serif

Colors

Designer to choose colors to be used in the design.

Requirements
Must have
• My logo, must bring attraction, picture attached of myself
Should not have
• Nothing that looks kidish

```html
<!DOCTYPE html>
<html lang="en">
<head>
<meta charset="utf-8">
<title>DJ Marlo Kvoss – Booking Flyer</title>
<link href="https://fonts.googleapis.com/css2?family=Archivo+Black&family=Oswald:wght@500;600&family=Poppins:wght@500&display=swap" rel="stylesheet">
<style>
  :root {
    --page: #eeeeee;
    --night: #0b0706;
    --ember: #e0461a;
    --flame: #f2792a;
    --brand-red: #e8231f;
    --white: #ffffff;
    --jacket: #1e1e21;
    --jacket-light: #3a3a3e;
    --icon-ig: #c13584;
    --icon-wave: #f26f1f;
    --icon-mail: #6b4bc4;
    --icon-phone: #4a5fd0;
  }
  * { margin: 0; padding: 0; box-sizing: border-box; }
  html, body {
    width: 1200px; height: 945px; overflow: hidden;
    background: var(--page);
  }
  .flyer {
    position: absolute; left: 33px; top: 30px;
    width: 1104px; height: 852px; overflow: hidden;
    background: var(--night);
  }
  .skyline {
    position: absolute; left: 0; top: 0; width: 100%; height: 300px;
    background:
      radial-gradient(ellipse 60% 50% at 35% 90%, rgba(242,121,42,.7), transparent 70%),
      linear-gradient(180deg, #17100d 0%, #3a1e10 50%, #7a3412 80%, var(--night) 100%);
  }
  .fire-band {
    position: absolute; left: 0; bottom: 0; width: 100%; height: 170px;
    background: linear-gradient(180deg, rgba(224,70,26,0) 0%, var(--ember) 30%, var(--flame) 65%, var(--ember) 100%);
  }
  .dj-photo {
    position: absolute; left: 0; top: 0; width: 1104px; height: 852px;
  }
  .brand-name {
    position: absolute; right: 57px; top: 118px;
    font-family: "Archivo Black", sans-serif;
    font-size: 92px; line-height: 1.08;
    color: var(--brand-red);
    text-align: right;
  }
  .tagline {
    position: absolute; left: 507px; top: 350px;
    font-family: "Poppins", sans-serif; font-weight: 500;
    font-size: 50px; line-height: 1.2; color: var(--white);
  }
  .contacts {
    position: absolute; left: 708px; top: 452px;
    list-style: none;
    font-family: "Oswald", sans-serif; font-weight: 500;
    font-size: 25px; color: var(--white);
  }
  .contacts li { display: flex; align-items: center; height: 50px; gap: 22px; }
  .contacts svg { width: 38px; height: 38px; flex: none; }
  .genres {
    position: absolute; left: 0; top: 762px; width: 100%;
    text-align: center;
    font-family: "Oswald", sans-serif; font-weight: 600;
    font-size: 36px; letter-spacing: 1px; color: var(--white);
  }
</style>
</head>
<body>
  <main class="flyer">
    <div class="skyline" role="img" aria-label="Night city skyline with orange glow and a cheering crowd silhouette"></div>
    <div class="fire-band"></div>
    <svg class="dj-photo" viewBox="0 0 1104 852" role="img" aria-label="Photo of the DJ in a black track jacket and headphones at a laptop on a DJ stand">
      <defs>
        <linearGradient id="photo-tone" x1="0" y1="0" x2="1" y2="1">
          <stop offset="0" stop-color="var(--jacket-light)"/>
          <stop offset="1" stop-color="var(--jacket)"/>
        </linearGradient>
      </defs>
      <path d="M252 172 C300 165 335 180 335 230 L340 345 L522 487 L657 472 L702 600 L687 757 L27 757 L42 360 C60 300 150 270 170 230 C175 190 210 172 252 172 Z" fill="url(#photo-tone)"/>
    </svg>

    <h1 class="brand-name">DJ MARLO<br>KVOSS</h1>
    <p class="tagline">Book the best!</p>

    <ul class="contacts">
      <li>
        <svg viewBox="0 0 40 40" aria-hidden="true"><circle cx="20" cy="20" r="16" fill="var(--icon-ig)"/></svg>
        <span>DJMARLOKVOSS</span>
      </li>
      <li>
        <svg viewBox="0 0 40 40" aria-hidden="true"><circle cx="20" cy="20" r="16" fill="var(--icon-wave)"/></svg>
        <span>wavecrate.com/djkvoss</span>
      </li>
      <li>
        <svg viewBox="0 0 40 40" aria-hidden="true">
          <rect x="4" y="10" width="32" height="22" rx="2" fill="none" stroke="var(--icon-mail)" stroke-width="3"/>
          <path d="M5 12 L20 23 L35 12" fill="none" stroke="var(--icon-mail)" stroke-width="3"/>
        </svg>
        <span>djkvoss478@mailbright.net</span>
      </li>
      <li>
        <svg viewBox="0 0 40 40" aria-hidden="true">
          <rect x="11" y="4" width="18" height="32" rx="3" fill="none" stroke="var(--icon-phone)" stroke-width="3"/>
          <circle cx="20" cy="30" r="2" fill="var(--icon-phone)"/>
        </svg>
        <span>(555) 204-7781</span>
      </li>
    </ul>

    <p class="genres">HIPHOP, R&amp;B, DANCEHALL, SOCA, POP, AND KOMPA</p>
  </main>
</body>
</html>
```